Business card and stationery for VIP parking
Velmor Bay s.r.o.
I need double sided standard sized Business Card [3.5" x 2"]
Please, be creatives
Professional
Milan Vesecky
CEO
Na Lukách 512/27, Prague
Czech Republic 164 00
milan.vesecky@velmorbay.cz
www.velmorbay.cz
The business card should be very creative, professional, using the logo's color combinations. I also need envelopes, folders and all stationery set.
Some picture.

```html
<!DOCTYPE html>
<html lang="en">
<head>
<meta charset="utf-8">
<title>Velmor Bay – Business Card</title>
<link rel="stylesheet" href="https://fonts.googleapis.com/css2?family=PT+Sans:wght@400;700&display=swap">
<style>
  :root {
    --page-bg: #e9e9ea;
    --card-light: #ffffff;
    --card-shade: #e2e3e5;
    --brand-red: #c8202f;
    --brand-blue: #1f4ea3;
    --mark-neutral: #b9bbc0;
    --ink: #3d3d3f;
    --ink-soft: #6a6a6d;
    --rule: #9a9a9d;
  }
  * { box-sizing: border-box; margin: 0; padding: 0; }
  html, body {
    width: 1200px; height: 901px; overflow: hidden;
    background: var(--page-bg);
    font-family: "PT Sans", Arial, sans-serif;
    color: var(--ink);
  }
  .sheet {
    width: 1200px; height: 901px;
    display: flex; flex-direction: column;
    align-items: center; justify-content: center; gap: 56px;
  }
  .card {
    width: 600px; height: 343px;
    border-radius: 22px;
    background: linear-gradient(160deg, var(--card-light) 0%, #f4f4f5 45%, var(--card-shade) 100%);
    box-shadow: 0 10px 28px rgba(0,0,0,.18);
    position: relative;
  }
  /* back side */
  .card--back { display: flex; flex-direction: column; align-items: center; justify-content: center; gap: 14px; }
  .brand-square {
    width: 64px; height: 64px; border-radius: 6px;
    background: var(--mark-neutral);
  }
  .back-domain { font-size: 19px; letter-spacing: 2px; color: var(--ink); }
  /* front side */
  .brand {
    position: absolute; top: 44px; left: 0; right: 0;
    display: flex; align-items: center; justify-content: center; gap: 12px;
  }
  .brand .brand-square { width: 44px; height: 44px; border-radius: 5px; }
  .brand-name { font-size: 36px; font-weight: 700; color: var(--brand-blue); line-height: 1; }
  .details {
    position: absolute; top: 170px; left: 0; right: 0;
    display: flex; justify-content: center;
  }
  .person { text-align: right; padding: 8px 22px 0 0; width: 260px; }
  .person-name { font-size: 19px; font-weight: 700; color: var(--brand-red); }
  .person-role { font-size: 14px; color: var(--ink-soft); margin-top: 2px; }
  .divider { width: 1px; height: 132px; background: var(--rule); }
  .contact { padding-left: 22px; width: 290px; font-size: 14.5px; line-height: 1.25; }
  .address { margin-bottom: 8px; }
  .contact-row { display: flex; align-items: center; gap: 8px; }
  .contact-row svg { width: 13px; height: 13px; flex: none; fill: var(--ink-soft); }
</style>
</head>
<body>
<main class="sheet">
  <section class="card card--back" aria-label="Card back">
    <div class="brand-square"></div>
    <p class="back-domain">velmorbay.cz</p>
  </section>

  <section class="card card--front" aria-label="Card front">
    <div class="brand">
      <div class="brand-square"></div>
      <span class="brand-name">Velmor Bay</span>
    </div>
    <div class="details">
      <div class="person">
        <p class="person-name">Milan Vesecky</p>
        <p class="person-role">CEO</p>
      </div>
      <div class="divider"></div>
      <div class="contact">
        <p class="address">Na Lukách 512/27, Prague<br>Czech Republic 164 00</p>
        <p class="contact-row"><svg viewBox="0 0 16 16"><path d="M3 1h3l1.5 4-2 1.3a9 9 0 0 0 4.2 4.2L11 8.5l4 1.5v3a2 2 0 0 1-2 2A12 12 0 0 1 1 3a2 2 0 0 1 2-2z"/></svg>+420 210 555 318</p>
        <p class="contact-row"><svg viewBox="0 0 16 16"><path d="M4 0h8a1 1 0 0 1 1 1v14a1 1 0 0 1-1 1H4a1 1 0 0 1-1-1V1a1 1 0 0 1 1-1zm1 2v10h6V2zm3 11a1 1 0 1 0 0 2 1 1 0 0 0 0-2z"/></svg>+420 700 555 942</p>
        <p class="contact-row"><svg viewBox="0 0 16 16"><path d="M1 3h14v10H1zm1.5 1.2v.4L8 8.5l5.5-3.9v-.4zM2.5 6.3V11.8h11V6.3L8 10.2z"/></svg>milan.vesecky@velmorbay.cz</p>
        <p class="contact-row"><svg viewBox="0 0 16 16"><path d="M8 1a7 7 0 1 0 0 14A7 7 0 0 0 8 1zm0 1.5c.8 0 1.7 1.5 2 4H6c.3-2.5 1.2-4 2-4zM2.6 6.5h2c-.1.5-.1 1-.1 1.5s0 1 .1 1.5h-2a5.6 5.6 0 0 1 0-3zm3.4 3h4c-.3 2.5-1.2 4-2 4s-1.7-1.5-2-4zm5.4 0c.1-.5.1-1 .1-1.5s0-1-.1-1.5h2a5.6 5.6 0 0 1 0 3z"/></svg>www.velmorbay.cz</p>
      </div>
    </div>
  </section>
</main>
</body>
</html>
```